Postcard Design

Marlow Painting-all types of painting and staining-house,deck and roof powerwashing-stone and masonry sealing-
30 years in business-licensed and insured
Ray Pettibone
pettiboneworks@brushmail.example
9145820731

Industry/Entity Type

Painting

```html
<!DOCTYPE html>
<html lang="en">
<head>
<meta charset="utf-8">
<title>Marlow Painting Postcard</title>
<link rel="stylesheet" href="https://fonts.googleapis.com/css2?family=Fira+Sans:wght@400;500;600;700&family=Fira+Sans+Condensed:wght@500;600;700&display=swap">
<style>
  :root {
    --purple: #5b3f72;
    --purple-deep: #4a3160;
    --red: #d7263d;
    --green: #5cb82e;
    --gold: #d9a21b;
    --paint-green: #7ccc2a;
    --grey-light: #f4f4f4;
    --grey-mid: #d8d8d8;
    --ink: #222;
    --white: #fff;
  }
  * { box-sizing: border-box; margin: 0; padding: 0; }
  html, body { width: 991px; height: 1200px; overflow: hidden; background: #ffffff; }
  body { position: relative; font-family: "Fira Sans", Arial, sans-serif; }

  .card {
    position: absolute; width: 720px; height: 503px; overflow: hidden;
    box-shadow: 0 4px 14px rgba(0,0,0,.18);
  }
  .card--front { left: 40px; top: 48px; background: radial-gradient(ellipse at 65% 40%, var(--grey-light) 0%, var(--grey-mid) 100%); }
  .card--back { left: 231px; top: 640px; background: var(--white); }

  .abs { position: absolute; }

  /* Front */
  .front__photo {
    left: 0; top: 0; width: 300px; height: 381px;
    background: linear-gradient(100deg, var(--paint-green) 0%, #8fd63a 55%, rgba(143,214,58,0) 100%);
  }
  .services { font-weight: 600; white-space: nowrap; }
  .services__lead { color: var(--purple); }
  .services__list { color: var(--red); font-weight: 700; font-family: "Fira Sans Condensed", "Fira Sans", sans-serif; }
  .services__list .tick { color: var(--green); }
  .services__extra { color: var(--gold); }

  .front .services__lead { left: 254px; top: 32px; font-size: 16px; }
  .front .services__list { left: 254px; top: 54px; font-size: 27px; }
  .front .services__extra { left: 256px; top: 90px; font-size: 14px; }

  .years-badge {
    left: 564px; top: 29px; width: 88px; height: 118px;
    border: 3px solid var(--red); border-radius: 4px; background: var(--white);
    text-align: center; overflow: hidden;
  }
  .years-badge__num { font-family: "Fira Sans Condensed", sans-serif; font-weight: 700; color: var(--red); font-size: 60px; line-height: 66px; }
  .years-badge__label { background: var(--red); color: var(--white); font-weight: 700; font-size: 15px; line-height: 18px; padding: 5px 0 6px; }
  .years-badge__label small { display: block; font-size: 10px; font-weight: 600; line-height: 12px; }

  .brand { display: flex; align-items: center; gap: 12px; color: var(--purple); font-weight: 600; white-space: nowrap; }
  .brand__mark { background: var(--purple); }
  .front .brand { left: 340px; top: 262px; font-size: 40px; }
  .front .brand__mark { width: 18px; height: 18px; }

  .front__band {
    left: 0; top: 381px; width: 720px; height: 122px;
    background: linear-gradient(90deg, var(--purple) 0%, var(--purple-deep) 100%);
  }
  .front__band::before {
    content: ""; position: absolute; left: 0; top: 0; width: 100%; height: 4px;
    background: linear-gradient(90deg, var(--red), var(--gold), var(--green), #2b8fd6, var(--purple));
  }
  .front .owner { left: 28px; top: 442px; font-size: 31px; font-weight: 500; color: var(--white); }

  .contact { display: flex; align-items: center; gap: 12px; white-space: nowrap; font-weight: 500; }
  .contact svg { flex: none; }
  .front .contact { color: var(--white); font-size: 16px; left: 372px; }
  .front .contact--phone { top: 403px; font-size: 18px; }
  .front .contact--email { top: 446px; }

  /* Back */
  .back__wall {
    left: 0; top: 0; width: 720px; height: 230px;
    background: linear-gradient(180deg, #e9e9e7 0%, #f6f6f5 50%, rgba(255,255,255,0) 100%);
  }
  .back__photo {
    left: 0; top: 20px; width: 320px; height: 330px;
    background: linear-gradient(90deg, #cfdbe6 0%, #e6ecef 60%, rgba(255,255,255,0) 100%);
  }
  .promise {
    left: 108px; top: 40px; width: 400px; padding: 10px 14px 12px;
    background: rgba(91,63,114,.88); color: var(--white); white-space: nowrap;
  }
  .promise__quote { font-size: 16px; font-weight: 500; }
  .promise__years { font-size: 32px; font-weight: 700; line-height: 38px; }
  .promise__licensed { font-size: 26px; font-weight: 600; line-height: 30px; }

  .mail-label { color: var(--ink); font-size: 16px; text-align: center; line-height: 20px; }
  .mail-label--postage { left: 540px; top: 52px; }
  .mail-label--address { left: 452px; top: 196px; }
  .mail-label--barcode { left: 356px; top: 430px; }

  .back .services__lead { left: 57px; top: 250px; font-size: 15px; }
  .back .services__list { left: 57px; top: 268px; font-size: 24px; }
  .back .services__extra { left: 58px; top: 300px; font-size: 13px; }
  .back .contact { color: var(--purple); font-size: 14px; left: 150px; gap: 10px; }
  .back .contact--phone { top: 338px; }
  .back .contact--email { top: 362px; }
  .back .brand { left: 52px; top: 400px; font-size: 20px; gap: 8px; }
  .back .brand__mark { width: 10px; height: 10px; }
</style>
</head>
<body>

<section class="card card--front front" aria-label="Postcard front">
  <div class="abs front__photo" role="img" aria-label="Hand rolling bright green paint onto a wall with a paint roller"></div>

  <p class="abs services services__lead">All Types of PAINTING AND STAINING</p>
  <p class="abs services services__list"><span class="tick">✓</span>HOUSE <span class="tick">✓</span>DECK <span class="tick">✓</span>ROOF</p>
  <p class="abs services services__extra">Powerwashing-Stone and Masonry Sealing</p>

  <div class="abs years-badge">
    <div class="years-badge__num">30</div>
    <div class="years-badge__label">YEARS<small>IN BUSINESS</small></div>
  </div>

  <div class="abs brand"><span class="brand__mark"></span>Marlow Painting</div>

  <div class="abs front__band"></div>
  <p class="abs owner">Ray Pettibone</p>

  <p class="abs contact contact--phone">
    <svg width="20" height="28" viewBox="0 0 20 28" aria-hidden="true"><rect x="2" y="1.5" width="16" height="25" rx="3" fill="none" stroke="#fff" stroke-width="2.5"/><line x1="7" y1="22" x2="13" y2="22" stroke="#fff" stroke-width="2"/></svg>
    9145820731
  </p>
  <p class="abs contact contact--email">
    <svg width="24" height="22" viewBox="0 0 24 22" aria-hidden="true"><path d="M2 9 L12 2 L22 9 V20 H2 Z" fill="#fff"/><path d="M2 9 L12 15 L22 9" fill="none" stroke="#5b3f72" stroke-width="1.8"/></svg>
    pettiboneworks@brushmail.example
  </p>
</section>

<section class="card card--back back" aria-label="Postcard back">
  <div class="abs back__wall" role="img" aria-label="Textured white ceiling being painted"></div>
  <div class="abs back__photo" role="img" aria-label="Painter in white cap and shirt working on a ceiling"></div>

  <div class="abs promise">
    <p class="promise__quote">"No job is finished until you say it is!"</p>
    <p class="promise__years">30 years in business</p>
    <p class="promise__licensed">LICENSED AND INSURED</p>
  </div>

  <p class="abs mail-label mail-label--postage">Postage<br>Area</p>
  <p class="abs mail-label mail-label--address">Address Area</p>
  <p class="abs mail-label mail-label--barcode">Barcode Area</p>

  <p class="abs services services__lead">All Types of PAINTING AND STAINING</p>
  <p class="abs services services__list"><span class="tick">✓</span>HOUSE <span class="tick">✓</span>DECK <span class="tick">✓</span>ROOF</p>
  <p class="abs services services__extra">Powerwashing-Stone and Masonry Sealing</p>

  <p class="abs contact contact--phone">
    <svg width="14" height="20" viewBox="0 0 20 28" aria-hidden="true"><rect x="2" y="1.5" width="16" height="25" rx="3" fill="none" stroke="#d7263d" stroke-width="2.5"/><line x1="7" y1="22" x2="13" y2="22" stroke="#d7263d" stroke-width="2"/></svg>
    9145820731
  </p>
  <p class="abs contact contact--email">
    <svg width="16" height="15" viewBox="0 0 24 22" aria-hidden="true"><path d="M2 9 L12 2 L22 9 V20 H2 Z" fill="#d7263d"/><path d="M2 9 L12 15 L22 9" fill="none" stroke="#fff" stroke-width="1.8"/></svg>
    pettiboneworks@brushmail.example
  </p>

  <div class="abs brand"><span class="brand__mark"></span>Marlow Painting</div>
</section>

</body>
</html>
```